Swimming Pool Supply Company Business Cards

We need business cards designed for company. These need to be easy to edit so that we can fill in names, titles, and contact info for each person who works here.

Dalton R. Whitfield
Manager of Legal & Finance
K.L. Brisbane, Incorporated

4837 Grenway Avenue
Marlow Heights, PA 19243

E. dalton@klbrisbane-example.com
M. (215) 555-0173
O. (215) 555-0148

Contact Information for Business Card

Looking to upgrade current business cards with graphic that can be edited. Looking for fresh ideas for an age old industry.

Font styles to use
Serif
Sans Serif

Colors

Designer to choose colors to be used in the design.

Requirements
Must have
• Professional, fresh, unique but professional

```html
<!DOCTYPE html>
<html lang="en">
<head>
<meta charset="utf-8">
<title>Brisbane Business Cards</title>
<link href="https://fonts.googleapis.com/css2?family=Roboto:wght@300;400;700&display=swap" rel="stylesheet">
<style>
  :root {
    --backdrop: #adadad;
    --card: #fdfdfd;
    --brand-blue: #1f5cb6;
    --ink: #5a5a5a;
    --ink-soft: #6e6e6e;
  }
  html, body {
    margin: 0;
    padding: 0;
    width: 1200px;
    height: 960px;
    overflow: hidden;
    background: var(--backdrop);
    font-family: "Roboto", Arial, sans-serif;
  }
  .canvas {
    position: relative;
    width: 1200px;
    height: 960px;
  }
  .card {
    position: absolute;
    left: 320px;
    width: 560px;
    height: 320px;
    background: var(--card);
    box-shadow: 0 4px 14px rgba(0,0,0,0.18);
    box-sizing: border-box;
  }
  .card-front { top: 110px; }
  .card-back { top: 530px; }

  .brand {
    display: flex;
    flex-direction: column;
    align-items: flex-start;
    color: var(--brand-blue);
    white-space: nowrap;
  }
  .brand-name {
    font-weight: 700;
    line-height: 1;
  }
  .brand-tagline {
    font-weight: 700;
    text-transform: uppercase;
  }

  .card-front .brand {
    position: absolute;
    left: 24px;
    top: 144px;
    width: 172px;
  }
  .card-front .brand-name {
    font-size: 31px;
    letter-spacing: 0.8px;
  }
  .card-front .brand-tagline {
    font-size: 6px;
    letter-spacing: 0.3px;
    margin-top: 4px;
  }

  .divider {
    position: absolute;
    left: 214px;
    top: 40px;
    width: 1.5px;
    height: 240px;
    background: var(--brand-blue);
  }
  .contact {
    position: absolute;
    left: 242px;
    top: 38px;
    color: var(--ink);
    font-weight: 300;
    white-space: nowrap;
  }
  .contact p { margin: 0; }
  .person-name { font-size: 21px; color: #555; }
  .person-title { font-size: 13.5px; color: var(--ink-soft); margin-top: 2px !important; }
  .company { font-size: 16px; line-height: 1.35; margin-top: 34px !important; }
  .details { font-size: 16px; line-height: 1.7; margin-top: 26px !important; }

  .card-back .brand {
    position: absolute;
    right: 36px;
    bottom: 44px;
  }
  .card-back .brand-name {
    font-size: 40px;
    letter-spacing: 1px;
  }
  .card-back .brand-tagline {
    font-size: 8px;
    letter-spacing: 0.8px;
    margin-top: 5px;
  }
</style>
</head>
<body>
<main class="canvas">
  <section class="card card-front" aria-label="Business card front">
    <div class="brand">
      <span class="brand-name">BRISBANE</span>
      <span class="brand-tagline">Swimming Pools, Supplies &amp; Accessories</span>
    </div>
    <div class="divider"></div>
    <div class="contact">
      <p class="person-name">Dalton R. Whitfield</p>
      <p class="person-title">Manager of Legal &amp; Finance</p>
      <p class="company">K.L. Brisbane, Incorporated<br>4837 Grenway Avenue<br>Marlow Heights, PA 19243</p>
      <p class="details">E. dalton@klbrisbane-example.com<br>M. (215) 555-0173<br>O. (215) 555-0148</p>
    </div>
  </section>

  <section class="card card-back" aria-label="Business card back">
    <div class="brand">
      <span class="brand-name">BRISBANE</span>
      <span class="brand-tagline">Swimming Pools, Supplies &amp; Accessories</span>
    </div>
  </section>
</main>
</body>
</html>
```